Medical IT Business with New logo needs a fresh stationary design

First time on sketch Harbor; Thought I would give it a go.
This project is for business cards alone but we have loads of design work that needs to take place in the immediate future.

We provide IT services to the Medical Industry and value ourselves as offering a premium product to the market.

I am after a fresh, clean design using full colour 2 sided cards which includes our current colour palettes from our logo.

Card's must include:
- Logo
- Slogan
- Name
- Adress
- Email
- Phone
- Fax
- Mobile

Target Market(s)

Surgeons, High Profile Medical Personnel

Industry/Entity Type

Business

Fonts, CMYK Colours and Logo files attached.

Requirements
Must have
• Card's must include:
• - Logo
• - Slogan
• - Name
• - Adress
• - Email
• - Phone
• - Fax
• - Mobile
Nice to have
• Needs to incorporate our colour palette (attached CMYK colours)
Should not have
• Black backgrounds. Black text ok.

```html
<!DOCTYPE html>
<html lang="en">
<head>
<meta charset="utf-8">
<title>Clinara Systems – Business Card</title>
<link rel="stylesheet" href="https://fonts.googleapis.com/css2?family=Open+Sans:wght@400;600;700&display=swap">
<style>
  :root {
    --backdrop: #2b2b2d;
    --card: #f4f5f6;
    --brand-blue: #1b7fb5;
    --navy: #12305e;
    --ink: #555a60;
    --rule: #6f7378;
    --white: #ffffff;
  }
  * { margin: 0; padding: 0; box-sizing: border-box; }
  html, body {
    width: 1200px; height: 997px; overflow: hidden;
    background: var(--backdrop);
    font-family: "Open Sans", Arial, sans-serif;
  }
  .canvas { position: relative; width: 1200px; height: 997px; }
  .card {
    position: absolute; width: 640px; height: 366px;
    background: var(--card); border-radius: 22px; overflow: hidden;
  }
  /* Front */
  .card-front { left: 60px; top: 60px; }
  .front-disc {
    position: absolute; left: 60px; top: 63px;
    width: 240px; height: 240px; border-radius: 50%;
    background: var(--brand-blue);
  }
  .front-name {
    position: absolute; left: 330px; top: 150px;
    font-weight: 700; font-size: 34px; line-height: 1.1;
    letter-spacing: 1px; color: var(--brand-blue);
  }
  /* Back */
  .card-back { left: 500px; top: 480px; }
  .brand {
    position: absolute; right: 40px; top: 34px;
    display: flex; align-items: center; gap: 10px;
  }
  .brand-dot { width: 42px; height: 42px; border-radius: 50%; background: var(--brand-blue); }
  .brand-text { display: flex; flex-direction: column; }
  .brand-name { font-weight: 700; font-size: 19px; color: var(--navy); letter-spacing: .5px; line-height: 1.1; }
  .brand-slogan { font-size: 9px; color: var(--ink); }
  .divider {
    position: absolute; left: 260px; right: 40px; top: 104px;
    height: 1px; background: var(--rule);
  }
  .person { position: absolute; left: 40px; top: 170px; }
  .person-name { font-weight: 700; font-size: 22px; color: var(--navy); line-height: 1.1; }
  .person-role { font-size: 17px; color: var(--brand-blue); line-height: 1.2; }
  .contacts { position: absolute; left: 40px; top: 230px; list-style: none; }
  .contacts li {
    display: flex; align-items: center; gap: 8px;
    font-size: 15px; color: var(--ink); height: 23px;
  }
  .contacts svg { width: 17px; height: 17px; flex: none; }
  .website {
    position: absolute; right: 40px; top: 300px;
    font-weight: 700; font-size: 15px; color: var(--brand-blue);
  }
</style>
</head>
<body>
<main class="canvas">
  <section class="card card-front" aria-label="Card front">
    <div class="front-disc"></div>
    <p class="front-name">CLINARA<br>SYSTEMS</p>
  </section>

  <section class="card card-back" aria-label="Card back">
    <div class="brand">
      <div class="brand-dot"></div>
      <div class="brand-text">
        <span class="brand-name">CLINARA SYSTEMS</span>
        <span class="brand-slogan">connected to your clinic</span>
      </div>
    </div>
    <div class="divider"></div>

    <div class="person">
      <p class="person-name">Owen Marlow</p>
      <p class="person-role">Director</p>
    </div>

    <ul class="contacts">
      <li>
        <svg viewBox="0 0 20 20" aria-label="Mobile"><circle cx="10" cy="10" r="10" fill="var(--brand-blue)"/><rect x="7" y="4.5" width="6" height="11" rx="1" fill="var(--white)"/></svg>
        6512034477
      </li>
      <li>
        <svg viewBox="0 0 20 20" aria-label="Phone"><circle cx="10" cy="10" r="10" fill="var(--brand-blue)"/><path d="M5 8 Q10 4 15 8 L14 10 L12 9 L12 8 Q10 7 8 8 L8 9 L6 10 Z M6 11 H14 V15 H6 Z" fill="var(--white)"/></svg>
        0561208833
      </li>
      <li>
        <svg viewBox="0 0 20 20" aria-label="Fax"><circle cx="10" cy="10" r="10" fill="var(--brand-blue)"/><rect x="7" y="4.5" width="6" height="4" fill="var(--white)"/><rect x="5" y="9" width="10" height="6" rx="1" fill="var(--white)"/></svg>
        0172049316
      </li>
      <li>
        <svg viewBox="0 0 20 20" aria-label="Email"><circle cx="10" cy="10" r="10" fill="var(--brand-blue)"/><rect x="5" y="6.5" width="10" height="7" fill="var(--white)"/><path d="M5 6.5 L10 10.5 L15 6.5" fill="none" stroke="var(--brand-blue)" stroke-width="1"/></svg>
        care@clinarasystems.com
      </li>
      <li>
        <svg viewBox="0 0 20 20" aria-label="Address"><circle cx="10" cy="10" r="10" fill="var(--brand-blue)"/><path d="M4.5 10 L10 5 L15.5 10 H14 V15 H6 V10 Z" fill="var(--white)"/></svg>
        Rm Unit 4B 210 Park Lane, Pune
      </li>
    </ul>

    <p class="website">www.clinarasystems.com</p>
  </section>
</main>
</body>
</html>
```